Brett Olsen Building Business Card Design

Hi,

I need a business card for my Building company.
I am a Builder and build homes for clients.
I am looking for a sophisticated logo that can be used on business cards, envelopes and letter heads.
I am trying to take my business to the next level and need a professional business card.

Colours: Please use white, black, dark grey and bright blue.

Thank you,

Carol and Brett.

Target Market(s)

1. Home and Building Companies 2. Potential customers

Industry/Entity Type

Business

Contact Information for Business Card

Brett Olsen Building PTY LTD

Brett Olsen

Director

A.B.N. 37 829 516 073

BUILDERS LICENCE No. 573019k

Mobile: 0412 907 381

Email: brettolsenbuilding@mailvane.com.au

Requirements
Must have
• The following is compulsory to have in the designs:

Brett Olsen Building PTY LTD (business name)

Brett Olsen (contact name)

Director (position)

A.B.N. 37 829 516 073

Builders Licence No. 573019k

Mobile: 0412 907 381

Nice to have
• Logo for business
Should not have
• Should not be cluttered.

I am looking for a clean, sophisticated and professional business card design.

```html
<!DOCTYPE html>
<html lang="en">
<head>
<meta charset="utf-8">
<title>Brett Olsen Building – Business Card</title>
<link href="https://fonts.googleapis.com/css2?family=Open+Sans:ital,wght@0,400;0,600;0,700;1,400&display=swap" rel="stylesheet">
<style>
  :root {
    --stage: #3b3b3b;
    --card-white: #ffffff;
    --card-dark: #221f20;
    --ink-dark: #2a2a2a;
    --ink-mid: #3c3c3c;
    --band-grey: #8c8c8c;
    --text-light: #ffffff;
  }
  * { margin: 0; padding: 0; box-sizing: border-box; }
  html, body {
    width: 1200px;
    height: 894px;
    overflow: hidden;
    background: var(--stage);
    font-family: "Open Sans", Arial, sans-serif;
  }
  .stage {
    position: relative;
    width: 1200px;
    height: 894px;
  }
  .card {
    position: absolute;
    width: 620px;
    height: 362px;
    box-shadow: 0 6px 18px rgba(0,0,0,0.45);
  }

  /* Front of card */
  .card-front {
    left: 470px;
    top: 80px;
    background: var(--card-white);
  }
  .wordmark {
    position: absolute;
    left: 82px;
    top: 150px;
    width: 456px;
    text-align: right;
  }
  .wordmark-name {
    display: block;
    font-weight: 600;
    font-size: 56px;
    line-height: 1;
    letter-spacing: 3px;
    color: var(--ink-dark);
    text-transform: uppercase;
  }
  .wordmark-tagline {
    display: block;
    margin-top: 6px;
    font-weight: 400;
    font-size: 23px;
    color: var(--ink-mid);
  }

  /* Back of card */
  .card-back {
    left: 110px;
    top: 452px;
    background: var(--card-dark);
    color: var(--text-light);
  }
  .contact {
    position: absolute;
    left: 40px;
    top: 58px;
  }
  .contact-name {
    font-size: 24px;
    font-weight: 700;
    margin-bottom: 14px;
  }
  .contact-role {
    font-weight: 400;
    font-style: italic;
  }
  .contact-line {
    display: flex;
    align-items: center;
    font-size: 24px;
    line-height: 1.25;
  }
  .contact-line svg {
    width: 30px;
    height: 22px;
    margin-right: 8px;
    flex: none;
  }
  .legal-band {
    position: absolute;
    left: 0;
    bottom: 0;
    width: 100%;
    height: 56px;
    background: var(--band-grey);
    display: flex;
    align-items: center;
    justify-content: center;
    font-size: 15px;
    color: var(--text-light);
  }
  .legal-band b { font-weight: 700; }
</style>
</head>
<body>
<main class="stage">

  <section class="card card-front" aria-label="Card front">
    <div class="wordmark">
      <span class="wordmark-name">Brett Olsen</span>
      <span class="wordmark-tagline">Building PTY LTD</span>
    </div>
  </section>

  <section class="card card-back" aria-label="Card back">
    <div class="contact">
      <p class="contact-name">Brett Olsen <span class="contact-role">Director</span></p>
      <p class="contact-line">
        <svg viewBox="0 0 30 22" aria-hidden="true">
          <path d="M2 7 Q15 -1 28 7 L25 10 L21 8 L20 5 Q15 3.5 10 5 L9 8 L5 10 Z" fill="#fff"/>
          <path d="M8 11 L10 8 H20 L22 11 L25 20 H5 Z" fill="#fff"/>
          <circle cx="15" cy="15" r="3" fill="#221f20"/>
        </svg>
        0412 907 381
      </p>
      <p class="contact-line">
        <svg viewBox="0 0 30 22" aria-hidden="true">
          <rect x="3" y="4" width="24" height="16" fill="#fff"/>
          <path d="M3 4 L15 14 L27 4" fill="none" stroke="#221f20" stroke-width="2"/>
        </svg>
        brettolsenbuilding@mailvane.com.au
      </p>
    </div>
    <footer class="legal-band">
      <span><b>ABN:</b> 37 829 516 073 &bull; <b>BUILDERS LICENCE No.:</b> 573019k</span>
    </footer>
  </section>

</main>
</body>
</html>
```